Business Card Design Project

Need a business card designed for a horse racing/gambling centered company.
Company name is BrightQuill.com.au
Company colours are similar to those in the logo.
Something clean and modern , designer given liberty to be creative.
Incorporate the logo is preferred.
Single or Double Sided fine
Must include :
Name
Mobile Number
Email Address
Reason: Apologies, I have been traveling unexpectedly with business and just need the extra two days to reply and give feedback before making a decision.
Industry/Entity Type
Business

```html
<!DOCTYPE html>
<html lang="en">
<head>
<meta charset="utf-8">
<title>BrightQuill.com.au Business Card</title>
<link rel="stylesheet" href="https://fonts.googleapis.com/css2?family=Arimo:wght@400;700&display=swap">
<style>
  :root {
    --card-dark: #1d1a0e;
    --card-dark-edge: #2a2513;
    --accent-red: #ee1c1c;
    --accent-red-deep: #c80f0f;
    --brand-teal: #2f8f78;
    --text-light: #ffffff;
  }
  html, body {
    margin: 0;
    padding: 0;
    width: 744px;
    height: 1200px;
    overflow: hidden;
    background: #ffffff;
  }
  .card {
    position: relative;
    width: 744px;
    height: 1200px;
    overflow: hidden;
    font-family: "Arimo", Arial, sans-serif;
  }
  .card-backdrop {
    position: absolute;
    inset: 0;
    background: radial-gradient(ellipse at 60% 35%, var(--card-dark-edge), var(--card-dark) 70%);
  }
  .card-band {
    position: absolute;
    inset: 0;
  }
  .brand {
    position: absolute;
    top: 80px;
    left: 0;
    width: 744px;
    display: flex;
    flex-direction: column;
    align-items: center;
    gap: 34px;
  }
  .brand-disc {
    width: 320px;
    height: 320px;
    border-radius: 50%;
    background: var(--brand-teal);
  }
  .brand-name {
    margin: 0;
    color: var(--text-light);
    font-weight: 700;
    font-size: 46px;
    line-height: 52px;
    letter-spacing: 1px;
  }
  .contact {
    position: absolute;
    right: 78px;
    top: 990px;
    text-align right;
    text-align: right;
    color: var(--text-light);
    font-size: 37px;
    line-height: 51px;
    font-weight: 400;
  }
  .contact p { margin: 0; white-space: nowrap; }
</style>
</head>
<body>
  <div class="card">
    <div class="card-backdrop" role="img" aria-label="Dark background with fine curved racetrack lines"></div>

    <svg class="card-band" width="744" height="1200" viewBox="0 0 744 1200" aria-hidden="true">
      <path d="M0 972 C 120 915, 260 890, 380 888 C 520 888, 650 905, 744 932 L 744 1200 L 0 1200 Z" fill="var(--accent-red)"/>
      <path d="M0 972 C 120 915, 260 890, 380 888 C 520 888, 650 905, 744 932" fill="none" stroke="var(--accent-red-deep)" stroke-width="4"/>
    </svg>

    <header class="brand">
      <div class="brand-disc" aria-hidden="true"></div>
      <p class="brand-name">BrightQuill.com.au</p>
    </header>

    <section class="contact">
      <p class="contact-name">Liam Carter</p>
      <p class="contact-phone">312.555.0148</p>
      <p class="contact-email">liam@brightquill.com</p>
    </section>
  </div>
</body>
</html>
```